Law Firm
To All Designers:
New e-mail address for the project is daniel@rvestlegal.net.
Thanks. I love all the designs.
P.S. I like the orange on the one side of the card as opposed to black.
@ph - New drafts #161 & #162 in lieu of 145 & 146 are submitted, Can you please check & provide feedback in private message.
Thanks
draft #145 and #146 Drafts came out black and I cannot see them (look like negatives). Please resubmit. Thanks.
Please DO NOT PUT "Gavels", "Scales of Justice" "Court Buildings", etc. on the card. I DO NOT WANT IT.
Thanks.
draft #130 Card looks a lot better. Can I see it with the dot at the end of the big line through the card a little smaller (but that is the look I was going for) and can I see some color (black, orange and/or grey) below that line where the address, phone and e-mail appear? Also, can I see with just the "m" and the line part of the logo on the other side? Thanks.
draft #125 and #126 Looks better. I didn't like the "watermark" "m" in my logo being sideways on the card (it didn't look like an "m" anymore to me that way), but Ido like it on the stationary and envelope. Can I see the card with the same orange on the one side with the orange line under the "m" in my logo at the bottom of the card then the address, telephone and e-mail below it? Thanks.
To all designers,
Can I start seeing letterhead, envelopes, fax covers and e-mail signatures too! I look forward to seeing the designs!
draft #49 I like the line under my name like in the logo. Can I see with orange on the other side of the card?
drafts #101, #102, #103 and #104 I would like to see with orange on the other side of the card rather than black
I like the use of the whites and oranges with black accents. So not too much black. I also like orange with the logo (either with the text or just the script "m") on one side of the card. Thanks for all the great designs.
draft #35 I like the use of the logo at the bottom of the card. But "no "scales of justice", "court buildings" or "gavels", etc. was not something I wanted on the card, it was just an instruction to the designers that although I am a lawyer, I do not want to use these symbols.
draft #31 and #32 Maybe you could use the orange line under the script "m" under the logo for the "white space"?
draft #31 and #32 Like the use of the colors in the card and the "watermark" logo on the stationary. However, there is too much "white space" on the right side of the card. Other drafts did better job with "white space". I would also like to maybe see the "watermark" logo used in the card as well.

```html
<!DOCTYPE html>
<html lang="en">
<head>
<meta charset="utf-8">
<title>Daniel R. Vest, P.C. — Stationery Set</title>
<link rel="stylesheet" href="https://fonts.googleapis.com/css2?family=Cinzel:wght@600&family=Open+Sans:wght@400;600&display=swap">
<style>
:root{
  --backdrop:#4a2c1a;
  --paper:#ffffff;
  --paper-shade:#f1f1f1;
  --orange:#f26a2e;
  --ink:#1e1e1e;
  --grey:#8a8a8a;
  --label:#d9c6b4;
}
*{margin:0;padding:0;box-sizing:border-box}
html,body{width:1200px;height:439px;overflow:hidden}
body{background:var(--backdrop);font-family:"Open Sans",sans-serif;position:relative}
.piece{position:absolute;box-shadow:0 2px 6px rgba(0,0,0,.45)}
.label{position:absolute;font-size:7px;color:var(--label);text-align:center}
.firm-name{font-family:"Cinzel",serif;font-weight:600;color:var(--ink);letter-spacing:.5px;white-space:nowrap}
.firm-rule{display:block;height:1px;background:var(--orange)}
.contact{font-size:5px;line-height:6.5px;color:var(--grey)}
.curve{position:absolute;left:0;bottom:0;width:100%}

/* business cards */
.card{width:112px;height:66px;left:18px;overflow:hidden}
.card-front{top:176px;background:var(--paper)}
.card-front .contact{position:absolute;right:8px;top:5px;text-align:right}
.card-front .holder{font-size:6px;line-height:7px;color:var(--orange);font-weight:600}
.card-back-orange{top:264px;background:var(--orange)}
.card-back-white{top:352px;background:var(--paper)}
.card-back-orange .firm-name,.card-back-white .firm-name{position:absolute;left:0;right:0;top:24px;text-align:center;font-size:9px}
.card-back-orange .firm-name{color:var(--paper)}

/* letterheads */
.letterhead{top:20px;width:216px;height:376px;background:var(--paper);overflow:hidden}
.letterhead-one{left:270px}
.letterhead-two{left:505px}
.letterhead .brand{position:absolute;top:20px;left:18px}
.letterhead .firm-name{font-size:11px}
.letterhead .contact{position:absolute;top:18px;right:16px}

/* envelopes */
.envelope{left:756px;width:424px;height:108px;background:var(--paper);overflow:hidden}
.env-back-white{top:28px;background:var(--paper-shade)}
.env-back-dark{top:86px}
.env-back-plain{top:168px;background:var(--paper-shade)}
.env-front{top:250px;left:748px;height:112px}
.envelope .flap{position:absolute;inset:0;width:100%;height:100%}
.env-front .brand{position:absolute;left:14px;top:14px}
.env-front .firm-name{font-size:13px}
</style>
</head>
<body>

<!-- business card: front -->
<div class="piece card card-front">
  <div class="contact">
    <div class="holder">Daniel R. Vest</div>
    <div>Attorney at Law</div>
    <div>(555) 014-2290</div>
    <div>daniel@rvestlegal.net</div>
    <div>www.qlzverne.com</div>
  </div>
  <svg class="curve" viewBox="0 0 112 20" preserveAspectRatio="none" height="20">
    <path d="M0 20 L0 17 Q56 3 112 7 L112 20 Z" fill="var(--orange)"/>
    <path d="M0 15 Q56 1 112 5" fill="none" stroke="var(--ink)" stroke-width="1.4"/>
  </svg>
</div>
<div class="label" style="left:18px;top:246px;width:112px">Front card</div>

<!-- business card: orange back -->
<div class="piece card card-back-orange">
  <div class="firm-name">Daniel R. Vest, P.C.</div>
</div>
<div class="label" style="left:18px;top:334px;width:112px">Back Card Option #1</div>

<!-- business card: white back -->
<div class="piece card card-back-white">
  <div class="firm-name">Daniel R. Vest, P.C.</div>
  <svg class="curve" viewBox="0 0 112 20" preserveAspectRatio="none" height="20">
    <path d="M0 18 Q56 0 112 6" fill="none" stroke="var(--ink)" stroke-width="1.4"/>
  </svg>
</div>
<div class="label" style="left:18px;top:422px;width:112px">Back Card Option #2</div>

<!-- letterhead one -->
<div class="piece letterhead letterhead-one">
  <div class="brand"><span class="firm-name">Daniel R. Vest, P.C.</span><span class="firm-rule"></span></div>
  <div class="contact">
    <div>123 Harbor Lane</div>
    <div>(555) 014-2290</div>
    <div>daniel@rvestlegal.net</div>
  </div>
  <svg class="curve" viewBox="0 0 216 40" preserveAspectRatio="none" height="40">
    <path d="M0 38 Q110 4 216 14" fill="none" stroke="var(--ink)" stroke-width="2"/>
    <path d="M0 40 L0 39 Q110 10 216 18 L216 40 Z" fill="var(--orange)" opacity=".15"/>
  </svg>
</div>
<div class="label" style="left:270px;top:402px;width:216px">Letterhead Option #1</div>

<!-- letterhead two -->
<div class="piece letterhead letterhead-two">
  <div class="brand"><span class="firm-name">Daniel R. Vest, P.C.</span><span class="firm-rule"></span></div>
  <svg class="curve" viewBox="0 0 216 50" preserveAspectRatio="none" height="50">
    <path d="M0 50 L0 34 Q110 6 216 16 L216 50 Z" fill="var(--orange)"/>
    <path d="M0 32 Q110 2 216 12" fill="none" stroke="var(--ink)" stroke-width="2"/>
  </svg>
</div>
<div class="label" style="left:505px;top:402px;width:216px">Letterhead Option #2</div>

<!-- envelopes -->
<div class="piece envelope env-back-white">
  <svg class="flap" viewBox="0 0 424 108" preserveAspectRatio="none">
    <path d="M0 0 L212 58 L424 0" fill="var(--paper)" stroke="#d6d6d6"/>
  </svg>
</div>
<div class="piece envelope env-back-dark">
  <svg class="flap" viewBox="0 0 424 108" preserveAspectRatio="none">
    <path d="M0 0 L212 62 L424 0 Z" fill="var(--ink)"/>
  </svg>
</div>
<div class="piece envelope env-back-plain">
  <svg class="flap" viewBox="0 0 424 108" preserveAspectRatio="none">
    <path d="M0 0 L212 58 L424 0" fill="var(--paper)" stroke="#d6d6d6"/>
  </svg>
</div>
<div class="piece envelope env-front">
  <div class="brand"><span class="firm-name">Daniel R. Vest, P.C.</span><span class="firm-rule"></span></div>
  <svg class="curve" viewBox="0 0 424 36" preserveAspectRatio="none" height="36">
    <path d="M0 36 L0 26 Q212 2 424 10 L424 36 Z" fill="var(--orange)"/>
    <path d="M0 24 Q212 0 424 8" fill="none" stroke="var(--ink)" stroke-width="2"/>
  </svg>
</div>
<div class="label" style="left:756px;top:372px;width:424px">Envelope Front &amp; Back</div>

</body>
</html>
```